Medical centre needs a business card

We are a medcial centre in Australia, needing a new business card. Our demographic is low working class families. We are going to be renovating our premises to modernise the look and also had a new logo done a few months ago representing quality and community, and now need to update our cards. It needs to be doubled sided, with logo and contact details on the front, and appointment details on the back. . Needs to be modern and simple, easy to read. <br/><br/>Name: Kindle Grove Medical Centre <br/>Address: 512 Tolvar Rd (Cnr Tolvar Rd & Quenby Park Rd),<br/>Dunmarra Court Shopping Centre, Paralowie, SA 5108<br/>Ph: 08 8194 3627<br/>Tag line: Where your care comes first<br/>Website: www.kindlegrovemedicalcentre-example.com.au<br/>Online bookings also available<br/><br/>(On the back, to have 3 lines of appointments that can be written in.<br/>Day, date, time)<br/><br/>Your next appointment is on<br/>Can try “M T W Th F Sa Su _________________ at ____________ am/pm” or other combinations <br/>Please advise as soon as possible if unable to attend<br/>Cancellation fees apply if less than 2 hrs notice<br/>Online appointments available (please highlight this option by either by position, colour or font)

Target Market(s)

Lower social economic working class, young families to seniors

Industry/Entity Type

Medical Centre

Contact Information for Business Card

Kindle Grove Medical Centre
512 Tolvar Rd (Cnr Tolvar Rd & Quenby Park Drive)
Dunmarra Court Shopping Centre
Hollin Vale SA 5921
Ph: 08 8194 3627
www.kindlegrovemedicalcentre-example.com.au
Tagline line: where your care comes first
Back side is for appointments
Your next appointment is with Dr ______________
Day/date/time (Please give 3 lines of appointments)
Please advise as soon as possible if unable to attend
Cancellation fees apply if less than 2 hours notice
Online appointments available
Book online easily and conveniently (please highlight online appointments)

Font styles to use
Serif
Sans Serif

Colors

Designer to choose colors to be used in the design.

Requirements
Must have
• Modern and simple
• Easy to ready
• Induces a wellbeing feeling
• Incorporate our logo colours and feel from logo
• Induces feeling of stability and security
Nice to have
• Attract attention
• Pleasant to look at
• Feeling of innovation
Should not have
• Loud clashing colours
• Overly luxurious feeling
• Overly artistic

```html
<!DOCTYPE html>
<html lang="en">
<head>
<meta charset="utf-8">
<title>Kindle Grove Medical Centre – Business Card</title>
<link rel="stylesheet" href="https://fonts.googleapis.com/css2?family=Montserrat:wght@400;500;600;700&family=Roboto:wght@400;500&display=swap">
<style>
  :root {
    --stage: #2a2a2b;
    --blue-deep: #0a6cc0;
    --blue-mid: #1f8fd6;
    --blue-light: #4fbfea;
    --green: #b3d45a;
    --white: #ffffff;
    --ink: #4a4a4a;
    --brand-blue: #1a6fc4;
  }
  * { box-sizing: border-box; margin: 0; padding: 0; }
  html, body { width: 1200px; height: 929px; overflow: hidden; }
  body {
    background: var(--stage);
    font-family: "Montserrat", sans-serif;
    display: flex; flex-direction: column; align-items: center; justify-content: center;
    gap: 56px;
  }
  .card {
    position: relative; width: 630px; height: 360px; overflow: hidden;
    border-radius: 3px;
  }

  /* Back side: appointment card */
  .card-back {
    background: linear-gradient(160deg, var(--blue-deep) 0%, var(--blue-mid) 45%, var(--blue-light) 100%);
    color: var(--white);
  }
  .appt-label {
    position: absolute; top: 34px; left: 50%; transform: translateX(-50%);
    background: var(--white); color: var(--blue-mid);
    font-weight: 500; font-size: 15px; letter-spacing: 0.06em;
    padding: 7px 26px; border-radius: 8px; white-space: nowrap;
  }
  .appt-fields { position: absolute; top: 96px; left: 44px; right: 44px; font-size: 15px; font-weight: 500; }
  .field-row { display: flex; align-items: flex-end; gap: 8px; height: 34px; }
  .field-row .fill { flex: 1; border-bottom: 2px dotted rgba(255,255,255,0.9); margin-bottom: 4px; }
  .field-row .gap { width: 16px; }
  .field-row .suffix { font-size: 13px; }
  .appt-notes {
    position: absolute; top: 180px; left: 0; right: 0; text-align: center;
    font-size: 14px; font-weight: 500; letter-spacing: 0.03em; line-height: 1.45;
    text-transform: uppercase;
  }
  .appt-notes .online { font-weight: 700; }
  .web-band {
    position: absolute; left: 0; right: 0; bottom: 0; height: 60px;
    background: var(--green);
    display: flex; align-items: center; justify-content: center; gap: 12px;
    font-weight: 700; font-size: 17px; letter-spacing: 0.02em; white-space: nowrap;
  }

  /* Front side: brand and contacts */
  .card-front { background: var(--white); color: var(--ink); }
  .brand { position: absolute; top: 60px; left: 48px; display: flex; align-items: center; gap: 14px; }
  .brand-mark { width: 40px; height: 40px; background: var(--brand-blue); border-radius: 3px; }
  .brand-name {
    color: var(--brand-blue); font-weight: 700; font-size: 27px; line-height: 1.1;
    text-transform: uppercase; letter-spacing: 0.01em;
  }
  .contact { position: absolute; top: 170px; left: 48px; font-family: "Roboto", sans-serif; font-size: 17px; line-height: 1.35; }
  .contact .address { margin-bottom: 8px; }
  .contact-line { display: flex; align-items: center; gap: 8px; }
  .contact-line svg { flex: none; }
  .tagline-band {
    position: absolute; left: 0; right: 0; bottom: 0; height: 50px;
    background: var(--brand-blue); color: var(--white);
    display: flex; align-items: center; padding-left: 48px;
    font-weight: 700; font-size: 19px; letter-spacing: 0.1em; text-transform: uppercase;
  }
</style>
</head>
<body>

<section class="card card-back" aria-label="Appointment side">
  <div class="appt-label">YOUR NEXT APPOINTMENT IS :</div>
  <div class="appt-fields">
    <div class="field-row"><span>Name :</span><span class="fill"></span></div>
    <div class="field-row"><span>DATE :</span><span class="fill"></span><span class="gap"></span><span>TIME :</span><span class="fill"></span><span class="suffix">AM/PM</span></div>
  </div>
  <p class="appt-notes">
    Please advise as soon as possible if unable to attend<br>
    Cancellation fees apply if less than 2 hours notice<br>
    <span class="online">Online appointments available</span><br>
    Book online easily and conveniently
  </p>
  <div class="web-band">
    <svg width="24" height="24" viewBox="0 0 24 24" fill="none" stroke="#fff" stroke-width="1.8" aria-hidden="true">
      <circle cx="12" cy="12" r="10"/><ellipse cx="12" cy="12" rx="4.5" ry="10"/><line x1="2" y1="12" x2="22" y2="12"/>
    </svg>
    <span>WWW.KINDLEGROVEMEDICALCENTRE-EXAMPLE.COM.AU</span>
  </div>
</section>

<section class="card card-front" aria-label="Contact side">
  <div class="brand">
    <span class="brand-mark"></span>
    <span class="brand-name">Kindle Grove<br>Medical Centre</span>
  </div>
  <div class="contact">
    <p class="address">512 Tolvar Rd (Cnr Tolvar Rd &amp; Quenby Park Drive)<br>Dunmarra Court Shopping Centre Hollin Vale SA 5921</p>
    <p class="contact-line">
      <svg width="14" height="14" viewBox="0 0 24 24" fill="#1a6fc4" aria-hidden="true"><path d="M6.6 10.8a15 15 0 0 0 6.6 6.6l2.2-2.2c.3-.3.7-.4 1-.2 1.1.4 2.3.6 3.6.6.6 0 1 .4 1 1V20c0 .6-.4 1-1 1A17 17 0 0 1 3 4c0-.6.4-1 1-1h3.5c.6 0 1 .4 1 1 0 1.3.2 2.5.6 3.6.1.3 0 .7-.2 1z"/></svg>
      08 8194 3627</p>
    <p class="contact-line">
      <svg width="14" height="14" viewBox="0 0 24 24" fill="#1a6fc4" aria-hidden="true"><path d="M2 5h20v14H2z M2 5l10 8 10-8" stroke="#fff" stroke-width="1.5"/></svg>
      info@kindlegrovemedicalcentre-example.com.au</p>
    <p class="contact-line">
      <svg width="14" height="14" viewBox="0 0 24 24" aria-hidden="true"><circle cx="12" cy="12" r="11" fill="#1a6fc4"/><ellipse cx="12" cy="12" rx="4" ry="11" fill="none" stroke="#fff" stroke-width="1.5"/></svg>
      www.kindlegrovemedicalcentre-example.com.au</p>
  </div>
  <div class="tagline-band">Where your care comes first</div>
</section>

</body>
</html>
```